Give my personal webpage more appeal!

I need my CV website improved - drmeganholt.com.au.
I am using the template KESTREL from pagecraftly. i would like to keep the already existing theme but am open to suggestions.
Please focus on imagery, colour scheme, and textures to enhance the appeal and look of the page.
The content is there, but now I need a designer to improve the look of my page.
I need styling, royalty-free unique modern images to make the page professional, personal and friendly.
I work in healthcare, so I'm a people person.
I teach professionals and I treat a lot of families.

Target Market(s)

Parents, Professional Healthcare providers

Number of Pages Required

1 page

Font styles to use
Serif
Sans Serif

Requirements
Must have
• My face - image at the top, all the information already contained in it.
• Links to the websites I manage such as my blog.
• One Page website.
• All the information it already contains with the ability to have more.
• Ideally, we would keep the same format for the page although I'm happy to expand column and change the page's structure with in the theme template KESTREL.
Nice to have
• The current KESTREL template. I would like to keep the already existing theme but am open to suggestions.
Should not have
• Multiple pages.

```html
<!DOCTYPE html>
<html lang="en">
<head>
<meta charset="utf-8">
<title>Dr Megan Holt</title>
<link rel="stylesheet" href="https://fonts.googleapis.com/css2?family=Montserrat:wght@300;400;600;700;800&family=Open+Sans:wght@400;600&display=swap">
<style>
:root{
  --orange:#eca41d;
  --orange-deep:#c98a1b;
  --orange-band:#b8801f;
  --ink:#2e2e2e;
  --grey:#777;
  --line:#dcdcdc;
  --paper:#ffffff;
  --mist:#eeeeee;
}
*{box-sizing:border-box;margin:0;padding:0}
html,body{width:1200px;height:5248px;overflow:hidden;background:var(--paper)}
body{font-family:"Open Sans",Arial,sans-serif;color:var(--ink);font-size:12px;line-height:1.6;position:relative}
h1,h2,h3,h4,.nav,.btn{font-family:"Montserrat",Arial,sans-serif}

/* sidebar */
.sidebar{position:absolute;left:0;top:0;width:255px;height:648px;background:var(--paper);padding:46px 0 0 40px}
.brand{font-family:"Montserrat",sans-serif;font-weight:400;font-size:22px;color:var(--orange);letter-spacing:.5px}
.brand-sub{font-size:8px;color:var(--grey);margin:2px 0 0 70px;letter-spacing:1px}
.nav{list-style:none;margin-top:44px}
.nav li{font-size:9px;font-weight:700;letter-spacing:1.5px;color:var(--ink);margin-bottom:22px;padding-left:14px;position:relative;line-height:1.4}
.nav li::before{content:"";position:absolute;left:0;top:4px;width:5px;height:5px;border-radius:50%;background:var(--orange)}
.social{display:flex;gap:12px;margin-top:4px}
.social span{width:9px;height:9px;border-radius:50%;background:var(--ink)}

/* shared */
.section{position:absolute;left:255px;width:945px}
.photo{position:absolute;inset:0}
.heading{position:relative;display:flex;align-items:center;gap:16px;font-size:30px;font-weight:700;letter-spacing:1px;color:var(--orange)}
.heading::before{content:"";width:18px;height:4px;background:var(--orange)}
.heading.light{color:#fff}
.heading.light::before{background:#fff}

/* hero */
.hero{top:0;height:648px;overflow:hidden}
.hero .photo{background:radial-gradient(circle at 30% 70%,#f6d24a 0,#c9b33a 18%,transparent 40%),radial-gradient(circle at 80% 30%,#8fb64a 0,transparent 45%),linear-gradient(160deg,#6f9a3a,#a7b84a 45%,#d7b54a 70%,#7c8c3a)}
.hero .figure{position:absolute;left:300px;top:0;width:360px;height:648px;background:linear-gradient(180deg,#c78b6b 0,#b6765a 40%,#d0242d 58%,#c61f28 100%);border-radius:160px 160px 0 0;opacity:.9}
.hero .title{position:absolute;left:0;right:0;top:418px;text-align:center;color:#fff}
.hero .title p{font-family:"Montserrat",sans-serif;font-weight:300;font-size:40px;letter-spacing:2px;line-height:1.1}
.hero .title h1{font-size:56px;font-weight:700;letter-spacing:2px;line-height:1.1}
.btn{display:inline-block;margin-top:16px;background:var(--orange);color:var(--ink);font-size:9px;font-weight:700;letter-spacing:1.5px;padding:8px 30px}

/* about */
.about{top:648px;height:514px;overflow:hidden;background:var(--mist)}
.about .photo{left:380px;background:linear-gradient(90deg,var(--mist),#d8d8d8 40%,#cfcfcf 70%,#e2e2e2)}
.about .heading{position:absolute;left:115px;top:110px}
.about .text{position:absolute;left:145px;top:168px;width:320px;color:#555;font-size:12.5px;line-height:1.75}
.about .text p+p{margin-top:16px}

/* skills */
.skills{top:1162px;height:721px;overflow:hidden}
.skills .photo{background:linear-gradient(135deg,#b97d1c,#d79a2a 40%,#c08722 70%,#a9741a)}
.skills .heading{position:absolute;left:115px;top:148px}
.skill-grid{position:absolute;left:145px;top:240px;width:745px;display:grid;grid-template-columns:repeat(3,1fr);column-gap:45px;row-gap:50px;color:#fff}
.skill h3{display:flex;align-items:center;gap:8px;font-size:12px;font-weight:700;letter-spacing:1px;margin-bottom:10px}
.skill h3 svg{flex:none}
.skill p{font-size:9.5px;line-height:1.6;opacity:.95}

/* experiences */
.exp{top:1883px;height:1110px;background:var(--paper)}
.exp .heading{position:absolute;left:115px;top:70px}
.accordion{position:absolute;left:147px;top:130px;width:743px}
.acc-row{height:49px;border:1px solid var(--line);display:flex;align-items:center;padding:0 20px;gap:22px;font-size:10px;color:#999;margin-bottom:12px;position:relative}
.acc-row::after{content:"+";position:absolute;right:18px;top:14px;font-size:14px;color:#999}
.acc-row.open{background:var(--orange);border-color:var(--orange);color:var(--ink);font-weight:700;height:44px;margin-bottom:0}
.acc-row.open::after{content:"–";color:var(--ink)}
.acc-body{padding:26px 20px 34px;font-size:10px;color:#666;line-height:1.8;margin-bottom:12px}

/* education */
.edu{top:2993px;height:630px;overflow:hidden}
.edu .photo{background:linear-gradient(150deg,#a8741d,#d39a2c 45%,#c48a24 75%,#a36f1b)}
.edu .heading{position:absolute;left:115px;top:72px}
.edu .intro{position:absolute;left:147px;top:125px;width:680px;color:#fff;font-size:10px;opacity:.95}
.edu-grid{position:absolute;left:147px;top:215px;width:620px;display:grid;grid-template-columns:1fr 1fr;row-gap:40px;column-gap:40px;color:#fff}
.edu-item{display:flex;gap:18px;align-items:flex-start}
.edu-item .num{font-family:"Montserrat",sans-serif;font-size:56px;font-weight:700;line-height:1}
.edu-item p{font-size:9px;line-height:1.7;text-transform:uppercase;padding-top:4px}
.edu-quote{position:absolute;left:147px;top:530px;display:flex;gap:22px;color:#fff;align-items:center}
.edu-quote p{font-size:9px;text-transform:uppercase;line-height:1.6}

/* employment */
.emp{top:3623px;height:525px;overflow:hidden;background:var(--paper)}
.emp .photo{top:240px;background:linear-gradient(180deg,rgba(255,255,255,1),#e6e6e6 50%,#d4d4d4)}
.emp .heading{position:absolute;left:115px;top:70px}
.emp-grid{position:absolute;left:147px;top:150px;width:760px;display:grid;grid-template-columns:repeat(4,1fr);column-gap:38px}
.job h4{font-size:9px;color:var(--orange);font-weight:700;letter-spacing:.5px;line-height:1.4}
.job .role{font-size:8.5px;color:var(--ink);font-weight:600;text-transform:uppercase;margin:2px 0 8px}
.job .date{display:inline-block;background:var(--orange);color:var(--ink);font-size:8px;font-weight:700;padding:3px 12px;margin-bottom:10px}
.job p{font-size:9px;color:#444;line-height:1.65}

/* sites */
.sites{top:4148px;height:367px;background:var(--paper)}
.sites .heading{position:absolute;left:115px;top:58px}
.site-row{position:absolute;left:147px;top:160px;width:745px;display:flex;justify-content:space-between;align-items:center}
.site{width:150px;height:140px;display:flex;align-items:center;justify-content:center;font-family:"Montserrat",sans-serif;font-weight:700;font-size:16px;text-align:center;color:var(--ink)}
.site.dark{background:#1c1c1c;color:#fff}
.site.orange{color:var(--orange)}

/* contact */
.contact{top:4515px;height:490px;overflow:hidden}
.contact .photo{background:linear-gradient(135deg,#a8701a,#c8901f 50%,#b97f1c)}
.contact .heading{position:absolute;left:115px;top:68px}
.address{position:absolute;left:147px;top:135px;display:flex;gap:12px;color:#fff;font-size:9px;line-height:1.5}
.address strong{font-weight:700;letter-spacing:.5px}
.form{position:absolute;left:147px;top:195px;width:355px}
.form .pair{display:flex;gap:8px}
.field{height:30px;border:1px solid rgba(255,255,255,.8);color:#fff;font-size:9px;padding:8px 10px;margin-bottom:10px;flex:1}
.field.area{height:82px}
.submit{display:inline-block;background:#fff;color:var(--ink);font-family:"Montserrat",sans-serif;font-size:9px;font-weight:700;letter-spacing:1px;padding:7px 40px;margin-top:6px}

/* footer */
.footer{top:5005px;height:243px;background:linear-gradient(90deg,#f2f2f2,#fafafa 50%,#efefef);text-align:center;padding-top:60px}
.footer .brand{font-size:26px}
.footer .brand-sub{margin:2px 0 0}
.footer .social{justify-content:center;gap:26px;margin-top:22px}
.footer .social span{background:var(--orange);width:11px;height:11px}
.copy{font-size:9px;letter-spacing:1px;color:var(--ink);margin-top:18px;font-weight:600}
</style>
</head>
<body>

<aside class="sidebar">
  <div class="brand">dr Megan Holt</div>
  <div class="brand-sub">CHIROPRACTOR</div>
  <ul class="nav">
    <li>ABOUT ME</li>
    <li>SKILLS</li>
    <li>PROFESSIONAL<br>EXPERIENCES</li>
    <li>EDUCATION</li>
    <li>EMPLOYMENT</li>
    <li>SITES</li>
    <li>BLOG</li>
    <li>CONTACT</li>
  </ul>
  <div class="social"><span></span><span></span></div>
</aside>

<section class="section hero">
  <div class="photo" role="img" aria-label="Portrait of Dr Megan Holt in a red jacket against a green and yellow garden background"></div>
  <div class="figure" role="img" aria-label="Dr Megan Holt portrait placeholder"></div>
  <div class="title">
    <p>WELCOME, TO MY PAGE,</p>
    <h1>I AM DR MEGAN HOLT</h1>
    <span class="btn">SEE MORE BELOW</span>
  </div>
</section>

<section class="section about">
  <div class="photo" role="img" aria-label="Soft faded photo of a healthcare practitioner at work"></div>
  <h2 class="heading">ABOUT ME</h2>
  <div class="text">
    <p>Hello, I am a Chiropractor and a Diplomate of the Institute of Applied Movement Practice (IAMP). I am also on the board of certified teachers for the IAMP. Teaching engagements take me to local, national and international destinations. Thank you for visiting my page. I look forward to sharing some of my insights with you via my blog.</p>
    <p>I am born and bred here in Brisbane, Australia and now this city I call home.</p>
  </div>
</section>

<section class="section skills">
  <div class="photo" role="img" aria-label="Doctor with stethoscope under a warm orange overlay"></div>
  <h2 class="heading light">SKILLS</h2>
  <div class="skill-grid">
    <div class="skill">
      <h3><svg width="16" height="14" viewBox="0 0 16 14"><rect x="1" y="4" width="14" height="9" fill="#fff"/><rect x="5" y="1" width="6" height="3" fill="none" stroke="#fff" stroke-width="1.5"/></svg>BUSINESS DEVELOPMENT</h3>
      <p>I founded and grew a busy family practice over many years. I guide new clinics with planning, team building and patient care systems so they can thrive and serve their communities well.</p>
    </div>
    <div class="skill">
      <h3><svg width="16" height="14" viewBox="0 0 16 14"><path d="M1 4 8 1l7 3-7 3z" fill="#fff"/><path d="M4 6v4c2 2 6 2 8 0V6" fill="#fff"/></svg>TEACHING</h3>
      <p>I run practical seminars for healthcare providers at home and abroad. My courses blend clear theory with hands-on technique so practitioners can apply new skills with confidence.</p>
    </div>
    <div class="skill">
      <h3><svg width="16" height="14" viewBox="0 0 16 14"><circle cx="8" cy="7" r="6" fill="#fff"/></svg>CHIROPRACTIC SKILLS</h3>
      <p>I offer gentle, whole-body care for babies, children, parents and seniors. Each treatment is tailored to the person, with careful assessment and a friendly, calm approach.</p>
    </div>
    <div class="skill">
      <h3><svg width="16" height="14" viewBox="0 0 16 14"><path d="M8 13 2 7a3.3 3.3 0 0 1 6-4 3.3 3.3 0 0 1 6 4z" fill="#fff"/></svg>MOTHER AND WIFE</h3>
      <p>Family comes first for me. Raising my children has shaped how I care for the parents and little ones who visit my clinic every week, with patience and warmth.</p>
    </div>
    <div class="skill">
      <h3><svg width="16" height="14" viewBox="0 0 16 14"><path d="M2 12 8 2l6 10z" fill="#fff"/></svg>PRODUCT LAUNCHING</h3>
      <p>I have helped bring new health resources to market, from course material to online programs, working with partners to share useful tools with a wide audience.</p>
    </div>
    <div class="skill">
      <h3><svg width="16" height="14" viewBox="0 0 16 14"><path d="M3 1h10v4a5 5 0 0 1-10 0z M6 10h4v3H6z" fill="#fff"/></svg>EVENT CO-ORDINATION</h3>
      <p>I plan and host conferences and workshops for practitioners, handling venues, speakers and schedules so every guest enjoys a smooth and rewarding experience.</p>
    </div>
  </div>
</section>

<section class="section exp">
  <h2 class="heading">PROFESSIONAL EXPERIENCES</h2>
  <div class="accordion">
    <div class="acc-row open"><svg width="14" height="14" viewBox="0 0 14 14"><path d="M2 12 12 2M5 12h7V5" fill="none" stroke="#2e2e2e" stroke-width="1.5"/></svg>2017</div>
    <div class="acc-body">Course Presenter – Practical Movement and Posture for Healthcare Providers, held in Brisbane and Sydney for the IAMP teaching faculty.<br><br>Presenting: Family Wellness Seminar – Session 1 &amp; 2, Brisbane.<br><br>Invited to present: Regional Practitioners Forum, Spring Conference 2017.</div>
    <div class="acc-row"><span>⟋</span>2016</div>
    <div class="acc-row"><span>⟋</span>2015</div>
    <div class="acc-row"><span>⟋</span>2014</div>
    <div class="acc-row"><span>⟋</span>2013</div>
    <div class="acc-row"><span>⟋</span>2012</div>
    <div class="acc-row"><span>⟋</span>2011</div>
    <div class="acc-row"><span>⟋</span>2010</div>
    <div class="acc-row"><span>⟋</span>2009</div>
    <div class="acc-row"><span>⟋</span>2008</div>
    <div class="acc-row"><span>⟋</span>2007</div>
    <div class="acc-row"><span>⟋</span>2006</div>
    <div class="acc-row"><span>⟋</span>2005</div>
  </div>
</section>

<section class="section edu">
  <div class="photo" role="img" aria-label="Practitioner holding a stethoscope under an orange overlay"></div>
  <h2 class="heading light">EDUCATION</h2>
  <p class="intro">Lifelong learning has shaped the way I care for my patients. These studies laid the groundwork for my clinical and teaching work, and I continue to study and grow each year.</p>
  <div class="edu-grid">
    <div class="edu-item"><span class="num">01</span><p>Institute of Applied<br>Movement Practice<br>Diplomate, Teaching Faculty</p></div>
    <div class="edu-item"><span class="num">02</span><p>Bachelor of Science<br>Master of Chiropractic<br>Riverbend University</p></div>
    <div class="edu-item"><span class="num">03</span><p>Riverbend University<br>Bachelor of Human Movement<br>Brisbane, Australia</p></div>
    <div class="edu-item"><span class="num">04</span><p>Senior Certificate<br>Brisbane High School</p></div>
  </div>
  <div class="edu-quote">
    <svg width="26" height="22" viewBox="0 0 26 22"><path d="M0 22V11C0 5 3 1 10 0v4C6 5 5 8 5 11h5v11zM16 22V11c0-6 3-10 10-11v4c-4 1-5 4-5 7h5v11z" fill="#fff"/></svg>
    <p>Ongoing study and professional<br>development each and every year</p>
  </div>
</section>

<section class="section emp">
  <div class="photo" role="img" aria-label="Faded photo of pills and medicine on a white surface"></div>
  <h2 class="heading">EMPLOYMENT</h2>
  <div class="emp-grid">
    <div class="job"><h4>HOLT FAMILY CLINIC</h4><div class="role">Founder, Chiropractor</div><span class="date">2005–2017</span><p>Opened and manage a family practice caring for parents, babies and working adults. I lead a small team and mentor graduates joining the clinic.</p></div>
    <div class="job"><h4>NORTHSIDE HEALTH CENTRE</h4><div class="role">Associate Chiropractor</div><span class="date">2002–2005</span><p>Treated a wide range of patients in a shared clinic and built strong links with local doctors and physios.</p></div>
    <div class="job"><h4>IAMP TEACHING FACULTY</h4><div class="role">Certified Teacher</div><span class="date">2008–NOW</span><p>Teach accredited courses to practitioners across Australia and overseas, and help shape the training program.</p></div>
    <div class="job"><h4>RIVERBEND UNIVERSITY</h4><div class="role">Guest Lecturer</div><span class="date">2010</span><p>Delivered lectures and clinical workshops to final year students on assessment and family care.</p></div>
  </div>
</section>

<section class="section sites">
  <h2 class="heading">MY SITES</h2>
  <div class="site-row">
    <div class="site orange">Dr Megan Blog</div>
    <div class="site dark">CalmNest</div>
    <div class="site">learnmovement<br>.com.au</div>
    <div class="site">Reset Clinic</div>
  </div>
</section>

<section class="section contact">
  <div class="photo" role="img" aria-label="Portrait of Dr Megan Holt under a warm orange overlay"></div>
  <h2 class="heading light">CONTACT</h2>
  <div class="address">
    <svg width="14" height="18" viewBox="0 0 14 18"><path d="M7 0a7 7 0 0 0-7 7c0 5 7 11 7 11s7-6 7-11a7 7 0 0 0-7-7z" fill="#fff"/><circle cx="7" cy="7" r="2.5" fill="#b97f1c"/></svg>
    <div><strong>ADDRESS HERE</strong><br>Brisbane</div>
  </div>
  <div class="form">
    <div class="pair"><div class="field">Your Name</div><div class="field">Your Email</div></div>
    <div class="field">Your Phone Number</div>
    <div class="field area">Your Message</div>
    <span class="submit">SUBMIT</span>
  </div>
</section>

<footer class="section footer">
  <div class="brand">dr Megan Holt</div>
  <div class="brand-sub">CHIROPRACTOR</div>
  <div class="social"><span></span><span></span></div>
  <p class="copy">© 2017 DR MEGAN HOLT</p>
</footer>

</body>
</html>
```